Law firm Seeks Modern and Engaging Site Redesign

Law firm seeks a new web site. Should be modern, but retaining existing logo. Needs to include contact section, professional bio, services offered, and contact information.

The site should be modern, responsive, and able to be SEO optimized.

The finished product should be coded in a Wordpress site, which I will provide. I can work with other platforms, including Wix, but WP is preferred.

Note the current site is https://www.tallowfieldlaw.example/#/home

Target Market(s)

Family Law Practice

Industry/Entity Type

Legal

Coding

Coded - Design and coding required

Number of Pages Required

4 page

Font styles to use
Sans Serif

Requirements
Must have
• Service description
Bio pages for partners
Contact Form
Awards/Publication page

```html
<!DOCTYPE html>
<html lang="en">
<head>
<meta charset="utf-8">
<title>Tallowfield Marsh Law</title>
<link href="https://fonts.googleapis.com/css2?family=Lato:wght@400;700&family=Lora:wght@400&display=swap" rel="stylesheet">
<style>
:root{
  --blue:#4f7ee0;
  --blue-dark:#2f6fc4;
  --ink:#222;
  --text:#555;
  --muted:#888;
  --line:#d8d8d8;
  --footer:#1c1f24;
  --white:#fff;
}
*{box-sizing:border-box;margin:0;padding:0}
html,body{width:1200px;height:4014px;overflow:hidden}
body{position:relative;font-family:"Lato",sans-serif;color:var(--text);background:var(--white)}
.abs{position:absolute}
.serif{font-family:"Lora",serif;font-weight:400;letter-spacing:2px;color:var(--ink)}
.btn{position:absolute;background:var(--blue);color:var(--white);font:700 14px "Lato",sans-serif;display:flex;align-items:center;justify-content:center;gap:6px;text-transform:uppercase}
/* header */
.topline{left:0;top:0;width:1200px;height:4px;background:var(--blue)}
.logo{font:400 26px "Lato",sans-serif;color:#666;display:flex;align-items:center;gap:10px;white-space:nowrap}
.logo .mark{width:10px;height:10px;background:var(--blue)}
.nav{left:418px;top:0;height:93px;display:flex;align-items:center;font:700 14px "Lato",sans-serif;color:var(--ink)}
.nav a{padding:0 20px;height:93px;display:flex;align-items:center;position:relative;text-decoration:none;color:inherit}
.nav a.active{color:var(--blue)}
.nav a.active:after{content:"";position:absolute;left:10px;right:10px;bottom:0;height:4px;background:var(--blue)}
/* hero */
.hero{left:0;top:93px;width:1200px;height:514px;background:linear-gradient(180deg,#4d6480 0%,#6f7f92 45%,#5a5248 75%,#3d3630 100%)}
.hero h1{position:absolute;top:150px;width:100%;text-align:center;font-size:52px;color:var(--white)}
.hero p{position:absolute;top:212px;left:215px;width:770px;text-align:center;color:var(--white);font-size:13.5px;line-height:26px}
.hero .pager{position:absolute;top:440px;width:100%;text-align:center;color:var(--white);font:14px "Lora",serif}
/* sections */
.eyebrow{color:var(--blue);font:700 14px "Lato",sans-serif;text-transform:uppercase;letter-spacing:.5px}
.body{font-size:13.5px;line-height:26px;text-align:justify}
.photo{position:absolute}
.list{list-style:none;font-size:14.5px;letter-spacing:.5px}
.list li{display:flex;align-items:center;gap:14px;height:26px}
.list svg{flex:none}
.sub{color:var(--blue);font:700 19px/26px "Lato",sans-serif;letter-spacing:1px;text-transform:uppercase}
/* partners */
.card{position:absolute;top:2144px;width:232px;text-align:center}
.card .pic{height:230px}
.card h3{margin-top:22px;font:700 18px "Lato",sans-serif;color:var(--ink);letter-spacing:.5px;white-space:nowrap}
.card .mail{margin-top:6px;font-size:11px;color:var(--blue);white-space:nowrap}
.card .soc{margin-top:14px;display:flex;justify-content:center;gap:8px}
.card .soc span{width:48px;height:48px;border-radius:50%;border:1px solid #999}
.card .soc span.on{background:var(--blue);border-color:var(--blue)}
/* awards */
.awards{left:0;top:2594px;width:1200px;height:452px;background:linear-gradient(180deg,#6e8fe6 0%,#5a80df 60%,#4f77d8 100%)}
.award{position:absolute;top:170px;width:220px;text-align:center;color:var(--white)}
.award .ring{margin:0 auto;width:150px;height:150px;border:5px solid rgba(255,255,255,.9);border-radius:50%;display:flex;flex-direction:column;align-items:center;justify-content:center;font:400 20px "Lora",serif}
.award .ring b{font:400 34px "Lora",serif}
.award h4{margin-top:12px;font:700 19px "Lato",sans-serif;letter-spacing:1px}
/* contact */
.field{position:absolute;border:1px solid var(--line);font-size:13px;color:#999;padding:0 20px;display:flex;align-items:center}
/* footer */
.footer{left:0;top:3619px;width:1200px;height:334px;background:linear-gradient(180deg,#2a2d33,#15171b);color:var(--white)}
.footer h5{position:absolute;top:88px;font:700 17px "Lato",sans-serif;text-transform:uppercase}
.footer ul{position:absolute;top:130px;list-style:none;font-size:14px;line-height:26px}
.footer li{display:flex;gap:12px;align-items:flex-start}
.dot{width:10px;height:10px;border-radius:50%;background:var(--white);margin-top:8px;flex:none}
.copy{left:0;top:3953px;width:1200px;height:61px;display:flex;align-items:center;justify-content:center;font-size:13px;color:#666}
</style>
</head>
<body>

<header>
  <div class="abs topline"></div>
  <div class="abs logo" style="left:109px;top:22px"><span class="mark"></span>Tallowfield Marsh</div>
  <nav class="abs nav">
    <a class="active">Home</a><a>About us</a><a>Services</a><a>Partners</a><a>Contact us</a><a>Awards/Publication</a>
    <a><svg width="14" height="14" viewBox="0 0 14 14"><circle cx="6" cy="6" r="4.5" fill="none" stroke="#222" stroke-width="2"/><path d="M9.5 9.5L13 13" stroke="#222" stroke-width="2"/></svg></a>
  </nav>
</header>

<section class="abs hero" role="img" aria-label="City skyline with a suspension bridge at dusk">
  <h1 class="serif">TALLOWFIELD MARSH LAW</h1>
  <p>Lorem ipsum dolor sit amet, consectetur adipiscing elit, sed do eiusmod tempor incididunt ut labore et dolore Ut enim ad minim veniam, quis nostrud exercitation ullamco</p>
  <div class="btn" style="left:456px;top:277px;width:288px;height:46px;font-weight:400">Find out how we can help you</div>
  <div class="pager">⟵ 1 of 3 ⟶</div>
</section>

<section>
  <div class="abs eyebrow" style="left:109px;top:703px">Get to know our firm</div>
  <h2 class="abs serif" style="left:109px;top:728px;font-size:30px;letter-spacing:1.5px;white-space:nowrap">ABOUT TALLOWFIELD MARSH</h2>
  <p class="abs body" style="left:111px;top:780px;width:486px">Lorem ipsum dolor sit amet, consectetur adipiscing elit, sed do eiusmod tempor incididunt ut labore et dolore magna aliqua. Ut enim ad minim veniam, quis nostrud exercitation ullamco laboris nisi ut aliquip ex ea commodo consequat. Duis aute irure dolor in reprehenderit in voluptate velit esse cillum dolore eu fugiat nulla pariatur. Excepteur sint occaecat cupidatat non proident, sunt in culpa qui officia deserunt mollit anim id est laborum.</p>
  <div class="btn" style="left:111px;top:952px;width:160px;height:47px">Learn more ⟶</div>
  <div class="abs" style="left:900px;top:671px;width:226px;height:362px;background:var(--blue)"></div>
  <div class="photo" style="left:648px;top:706px;width:440px;height:292px;background:linear-gradient(90deg,#cfd2d6,#e6e8ea 50%,#6b5a4a)" role="img" aria-label="The two founding partners standing in the firm's lobby"></div>
</section>

<section>
  <div class="photo" style="left:0;top:1098px;width:600px;height:410px;background:linear-gradient(135deg,#d9dde2,#c8b9a8 55%,#7c6a58)" role="img" aria-label="Senior couple shaking hands with an attorney"></div>
  <h2 class="abs serif" style="left:667px;top:1108px;font-size:35px">FAMILY LAW</h2>
  <div class="abs sub" style="left:667px;top:1152px;width:440px">Our firm accepts all kinds of family law matters, including:</div>
  <ul class="abs list" style="left:667px;top:1215px">
    <li><svg width="14" height="14" viewBox="0 0 14 14"><circle cx="7" cy="7" r="7" fill="#555"/><path d="M4 7l2 2 4-4" stroke="#fff" stroke-width="1.8" fill="none"/></svg>Divorce</li>
    <li><svg width="14" height="14" viewBox="0 0 14 14"><circle cx="7" cy="7" r="7" fill="#555"/><path d="M4 7l2 2 4-4" stroke="#fff" stroke-width="1.8" fill="none"/></svg>Child Custody</li>
    <li><svg width="14" height="14" viewBox="0 0 14 14"><circle cx="7" cy="7" r="7" fill="#555"/><path d="M4 7l2 2 4-4" stroke="#fff" stroke-width="1.8" fill="none"/></svg>Child Support</li>
    <li><svg width="14" height="14" viewBox="0 0 14 14"><circle cx="7" cy="7" r="7" fill="#555"/><path d="M4 7l2 2 4-4" stroke="#fff" stroke-width="1.8" fill="none"/></svg>Alimony</li>
    <li><svg width="14" height="14" viewBox="0 0 14 14"><circle cx="7" cy="7" r="7" fill="#555"/><path d="M4 7l2 2 4-4" stroke="#fff" stroke-width="1.8" fill="none"/></svg>Division of Assets and Liabilities</li>
    <li><svg width="14" height="14" viewBox="0 0 14 14"><circle cx="7" cy="7" r="7" fill="#555"/><path d="M4 7l2 2 4-4" stroke="#fff" stroke-width="1.8" fill="none"/></svg>Pre-nuptial agreements</li>
    <li><svg width="14" height="14" viewBox="0 0 14 14"><circle cx="7" cy="7" r="7" fill="#555"/><path d="M4 7l2 2 4-4" stroke="#fff" stroke-width="1.8" fill="none"/></svg>High-net worth and complex divorce cases</li>
    <li><svg width="14" height="14" viewBox="0 0 14 14"><circle cx="7" cy="7" r="7" fill="#555"/><path d="M4 7l2 2 4-4" stroke="#fff" stroke-width="1.8" fill="none"/></svg>Domestic violence</li>
  </ul>
  <div class="btn" style="left:670px;top:1438px;width:160px;height:47px">Learn more ⟶</div>
</section>

<section>
  <h2 class="abs serif" style="left:109px;top:1545px;font-size:35px">CRIMINAL LAW</h2>
  <div class="abs sub" style="left:109px;top:1589px;width:460px">Our firm accepts all kinds of criminal law matters, including:</div>
  <ul class="abs list" style="left:109px;top:1652px">
    <li><svg width="14" height="14" viewBox="0 0 14 14"><circle cx="7" cy="7" r="7" fill="#555"/><path d="M4 7l2 2 4-4" stroke="#fff" stroke-width="1.8" fill="none"/></svg>Assault</li>
    <li><svg width="14" height="14" viewBox="0 0 14 14"><circle cx="7" cy="7" r="7" fill="#555"/><path d="M4 7l2 2 4-4" stroke="#fff" stroke-width="1.8" fill="none"/></svg>Domestic Violence</li>
    <li><svg width="14" height="14" viewBox="0 0 14 14"><circle cx="7" cy="7" r="7" fill="#555"/><path d="M4 7l2 2 4-4" stroke="#fff" stroke-width="1.8" fill="none"/></svg>Drug Crimes</li>
    <li><svg width="14" height="14" viewBox="0 0 14 14"><circle cx="7" cy="7" r="7" fill="#555"/><path d="M4 7l2 2 4-4" stroke="#fff" stroke-width="1.8" fill="none"/></svg>DWI/DUI</li>
    <li><svg width="14" height="14" viewBox="0 0 14 14"><circle cx="7" cy="7" r="7" fill="#555"/><path d="M4 7l2 2 4-4" stroke="#fff" stroke-width="1.8" fill="none"/></svg>Sex Crimes</li>
    <li><svg width="14" height="14" viewBox="0 0 14 14"><circle cx="7" cy="7" r="7" fill="#555"/><path d="M4 7l2 2 4-4" stroke="#fff" stroke-width="1.8" fill="none"/></svg>Theft/Fraud Crimes</li>
    <li><svg width="14" height="14" viewBox="0 0 14 14"><circle cx="7" cy="7" r="7" fill="#555"/><path d="M4 7l2 2 4-4" stroke="#fff" stroke-width="1.8" fill="none"/></svg>Expungements</li>
  </ul>
  <div class="btn" style="left:112px;top:1850px;width:160px;height:47px">Learn more ⟶</div>
  <div class="photo" style="left:600px;top:1508px;width:600px;height:412px;background:radial-gradient(circle at 55% 45%,#6a6c70,#2a2b2e 70%,#161718)" role="img" aria-label="Hands in handcuffs behind a suited back"></div>
</section>

<section>
  <h2 class="abs serif" style="left:0;top:2010px;width:1200px;text-align:center;font-size:35px">OUR PARTNERS</h2>
  <p class="abs" style="left:210px;top:2064px;width:780px;text-align:center;font-size:13.5px;line-height:26px">Lorem ipsum dolor sit amet, consectetur adipiscing elit, sed do eiusmod tempor incididunt ut labore et dolore magna aliqua. Ut enim ad minim veniam, quis nostrud</p>
  <div class="card" style="left:111px"><div class="pic" style="background:linear-gradient(160deg,#c9c2b4,#5e6470)" role="img" aria-label="Portrait of partner Dorian P. Tallowfield"></div><h3>Dorian P. Tallowfield</h3><div class="mail">dtallowfield@tallowfieldlaw.example</div><div class="soc"><span></span><span class="on"></span><span></span></div></div>
  <div class="card" style="left:358px"><div class="pic" style="background:linear-gradient(160deg,#8a6d55,#2f2c2c)" role="img" aria-label="Portrait of partner Nathan R. Marsh"></div><h3>Nathan R. Marsh</h3><div class="mail">nmarsh@tallowfieldlaw.example</div><div class="soc"><span></span><span class="on"></span><span></span></div></div>
  <div class="card" style="left:606px"><div class="pic" style="background:linear-gradient(160deg,#a77a62,#3b3434)" role="img" aria-label="Portrait of partner Lena S. Whitcombe"></div><h3>Lena S. Whitcombe</h3><div class="mail">lwhitcombe@tallowfieldlaw.example</div><div class="soc"><span></span><span class="on"></span><span></span></div></div>
  <div class="card" style="left:855px"><div class="pic" style="background:linear-gradient(160deg,#7a4a34,#2b2422)" role="img" aria-label="Portrait of partner Celia V. Ostrander"></div><h3>Celia V. Ostrander</h3><div class="mail">costrander@tallowfieldlaw.example</div><div class="soc"><span></span><span class="on"></span><span></span></div></div>
</section>

<section class="abs awards">
  <h2 class="abs serif" style="left:0;top:95px;width:1200px;text-align:center;font-size:35px;color:var(--white)">OUR AWARDS</h2>
  <div class="award" style="left:88px"><div class="ring"><b>$</b>1,00,000</div><h4>Lorem ipsum dolor</h4></div>
  <div class="award" style="left:354px"><div class="ring"><b>$</b>1,00,000</div><h4>Lorem ipsum dolor</h4></div>
  <div class="award" style="left:621px"><div class="ring"><b>$</b>1,00,000</div><h4>Lorem ipsum dolor</h4></div>
  <div class="award" style="left:887px"><div class="ring"><b>$</b>1,00,000</div><h4>Lorem ipsum dolor</h4></div>
</section>

<section>
  <h2 class="abs serif" style="left:0;top:3130px;width:1200px;text-align:center;font-size:40px">CONTACT US</h2>
  <div class="field" style="left:262px;top:3210px;width:333px;height:52px">First name*</div>
  <div class="field" style="left:607px;top:3210px;width:332px;height:52px">Last name*</div>
  <div class="field" style="left:262px;top:3280px;width:333px;height:52px">Phone*</div>
  <div class="field" style="left:607px;top:3280px;width:332px;height:52px">Email Address*</div>
  <div class="field" style="left:262px;top:3348px;width:677px;height:104px;align-items:flex-start;padding-top:18px">Name*</div>
  <div class="abs" style="left:358px;top:3486px;font-size:13px;display:flex;align-items:center;gap:6px"><span style="width:11px;height:11px;border:1px solid #777"></span>Forget password</div>
  <div class="btn" style="left:517px;top:3467px;width:170px;height:52px;background:var(--blue-dark);letter-spacing:3px">Submit</div>
  <div class="abs" style="left:718px;top:3470px;width:194px;height:48px;border:1px solid var(--line);background:#f9f9f9;display:flex;align-items:center;gap:8px;padding-left:10px;font-size:9px;color:#333"><span style="width:16px;height:16px;border:2px solid #bbb;background:#fff"></span>I'm not a robot</div>
</section>

<footer class="abs footer">
  <div class="abs logo" style="left:109px;top:82px;color:var(--white)"><span class="mark"></span>Tallowfield Marsh</div>
  <p class="abs" style="left:110px;top:150px;width:250px;font-size:15px;line-height:26px">Lorem ipsum dolor sit amet, con sectetur adipiscing elit, sed do eiusmod tempor</p>
  <h5 style="left:441px">Navigate</h5>
  <ul style="left:441px"><li>» Home</li><li>» About us</li><li>» Services</li><li>» Partners</li><li>» Contact us</li></ul>
  <h5 style="left:637px">Contact us</h5>
  <ul style="left:637px;width:290px">
    <li><svg width="12" height="16" viewBox="0 0 12 16" style="margin-top:5px;flex:none"><path d="M6 0a6 6 0 0 1 6 6c0 4-6 10-6 10S0 10 0 6a6 6 0 0 1 6-6z" fill="#fff"/><circle cx="6" cy="6" r="2.2" fill="#222"/></svg><span>18 Meridian Plaza Drive Suite 410<br>Ashbrook, NJ 07999</span></li>
    <li style="margin-top:10px"><svg width="14" height="14" viewBox="0 0 14 14" style="margin-top:6px;flex:none"><path d="M3 0l3 3-2 2c1 2 3 4 5 5l2-2 3 3-2 3C6 14 0 8 0 2z" fill="#fff"/></svg><span>Phone : (555) 014-2231</span></li>
    <li style="margin-top:16px"><svg width="14" height="14" viewBox="0 0 14 14" style="margin-top:6px;flex:none"><rect x="0" y="4" width="14" height="10" fill="#fff"/><rect x="3" y="0" width="8" height="5" fill="#fff"/><rect x="3" y="8" width="8" height="2" fill="#222"/></svg><span>FAX : (555) 014-2290</span></li>
  </ul>
  <h5 style="left:966px">Social media</h5>
  <ul style="left:966px"><li><span class="dot"></span>Newsfeed</li><li><span class="dot"></span>Updates</li><li><span class="dot"></span>Circles</li><li><span class="dot"></span>Reviews</li><li><span class="dot"></span>Videos</li></ul>
</footer>
<div class="abs copy">© Copyrights 2020 Tallowfield Marsh Law | All Rights Reserved</div>

</body>
</html>
```